Outdoor Real Estate Sales Banner

It should say

742 Alderwick Street, East Boston
Coming Spring 2026
3 Luxury Condos
Experience refined living with elegant design and high-end finishes. Thoughtfully crafted for both comfort and sophistication.
Construction by V Construction
Now Accepting Reservations

Schedule Your Private Tour Today
Marisa Quellan, Mapleforth Realty | 617-555-0172 | Marisa@mapleforthcoast.com
Tobias Wrenley, Mapleforth Realty | 617-555-0189 | Tobias@mapleforthcoast.com

Target Market(s)

30-45

Industry/Entity Type

real estate

Font styles to use
Serif

Requirements
Must have
• Colors of logo and preppy rich look
Nice to have
• herringbone incorporated the pattern
Should not have
• any loud colors

```html
<!DOCTYPE html>
<html lang="en">
<head>
<meta charset="utf-8">
<title>742 Alderwick Street – Sales Banner</title>
<link rel="stylesheet" href="https://fonts.googleapis.com/css2?family=Cinzel:wght@500;600;700&family=Crimson+Text:wght@400;600;700&family=Montserrat:wght@300;400&display=swap">
<style>
  :root {
    --navy: #111f3b;
    --navy-light: #1a2a4a;
    --gold: #e6b264;
    --white: #ffffff;
    --sand: #dcc58e;
    --photo-green: #7f9a6a;
    --photo-warm: #b9a79a;
  }
  * { margin: 0; padding: 0; box-sizing: border-box; }
  html, body { width: 863px; height: 1200px; overflow: hidden; }
  body { background: var(--navy); }
  .banner {
    position: relative;
    width: 863px;
    height: 1200px;
    background: radial-gradient(ellipse at center, var(--navy) 55%, var(--navy-light) 100%);
    color: var(--white);
    font-family: "Cinzel", serif;
  }
  .abs { position: absolute; }
  .centered { left: 0; right: 0; text-align: center; }

  .brand-mark { left: 370px; top: 54px; }
  .brand-name {
    top: 205px;
    font-family: "Cinzel", serif;
    font-weight: 600;
    font-size: 31px;
    letter-spacing: 1px;
    color: var(--gold);
  }
  .address {
    top: 277px;
    font-weight: 600;
    font-size: 30px;
    color: var(--white);
  }
  .launch-pill {
    left: 162px; top: 333px;
    width: 540px; height: 66px;
    border: 1.5px solid var(--white);
    border-radius: 33px;
    display: flex; align-items: center; justify-content: center;
    font-weight: 700;
    font-size: 36px;
    color: var(--gold);
    letter-spacing: 0.5px;
  }
  .rendering-frame {
    left: 264px; top: 427px;
    width: 335px; height: 342px;
    border: 8px solid var(--gold);
    background: var(--white);
    padding: 14px 20px;
  }
  .rendering {
    width: 100%; height: 100%;
    background: linear-gradient(180deg, var(--sand) 0%, #d2b97e 100%);
  }
  .headline {
    top: 780px;
    font-weight: 600;
    font-size: 68px;
    color: var(--gold);
    line-height: 1;
  }
  .intro {
    top: 862px;
    font-family: "Montserrat", sans-serif;
    font-weight: 300;
    font-size: 18px;
    line-height: 25px;
    color: var(--white);
  }
  .portrait {
    top: 950px;
    width: 133px; height: 190px;
    border: 3px solid var(--gold);
  }
  .portrait-left { left: 63px; background: linear-gradient(160deg, var(--photo-green), #3a4a6a 70%); }
  .portrait-right { left: 667px; background: linear-gradient(160deg, var(--photo-warm), #2a2a2a 75%); }
  .builder {
    left: 270px; width: 323px; top: 953px;
    padding-bottom: 4px;
    border-bottom: 1px solid rgba(230,178,100,0.5);
    text-align: center;
    font-weight: 500;
    font-size: 13.5px;
    color: var(--gold);
  }
  .reservations {
    top: 983px;
    font-family: "Crimson Text", serif;
    font-weight: 600;
    font-size: 23px;
  }
  .contact-rule { left: 196px; top: 1024px; width: 471px; height: 2px; background: var(--gold); }
  .contact-divider { left: 431px; top: 1027px; width: 1px; height: 109px; background: var(--gold); }
  .agent {
    top: 1046px; width: 220px;
    text-align: center;
    font-family: "Crimson Text", serif;
  }
  .agent-left { left: 215px; }
  .agent-right { left: 437px; }
  .agent-name { font-weight: 700; font-size: 17px; color: var(--gold); line-height: 18px; }
  .agent-firm { font-size: 12px; line-height: 14px; }
  .agent-phone { font-weight: 700; font-size: 18px; margin-top: 12px; line-height: 20px; }
  .agent-email { font-size: 10px; line-height: 12px; }
  .tour-call {
    top: 1156px;
    font-family: "Crimson Text", serif;
    font-weight: 600;
    font-size: 21px;
  }
</style>
</head>
<body>
<main class="banner">
  <svg class="abs brand-mark" width="123" height="123" viewBox="0 0 123 123" aria-hidden="true">
    <circle cx="61.5" cy="61.5" r="59" fill="none" stroke="var(--gold)" stroke-width="4"/>
  </svg>
  <div class="abs centered brand-name">MAPLEFORTH REALTY</div>

  <h1 class="abs centered address" style="font-weight:600">742 ALDERWICK STREET, EAST BOSTON</h1>
  <div class="abs launch-pill">COMING SPRING 2026</div>

  <div class="abs rendering-frame">
    <div class="rendering" role="img" aria-label="Front elevation rendering of the three-storey condo building"></div>
  </div>

  <h2 class="abs centered headline" style="font-weight:600">3 LUXURY CONDOS</h2>
  <p class="abs centered intro">Experience refined living with elegant design and high-end finishes.<br>Thoughtfully crafted for both comfort and sophistication.</p>

  <div class="abs portrait portrait-left" role="img" aria-label="Portrait photo of agent Tobias Wrenley"></div>
  <div class="abs portrait portrait-right" role="img" aria-label="Portrait photo of agent Marisa Quellan"></div>

  <div class="abs builder">CONSTRUCTION BY V CONSTRUCTION</div>
  <div class="abs centered reservations">Now Accepting Reservations</div>
  <div class="abs contact-rule"></div>
  <div class="abs contact-divider"></div>

  <div class="abs agent agent-left">
    <div class="agent-name">Tobias Wrenley</div>
    <div class="agent-firm">Mapleforth Realty</div>
    <div class="agent-phone">617-555-0189</div>
    <div class="agent-email">Tobias@mapleforthcoast.com</div>
  </div>
  <div class="abs agent agent-right">
    <div class="agent-name">Marisa Quellan</div>
    <div class="agent-firm">Mapleforth Realty</div>
    <div class="agent-phone">617-555-0172</div>
    <div class="agent-email">Marisa@mapleforthcoast.com</div>
  </div>

  <div class="abs centered tour-call">Schedule Your Private Tour Today</div>
</main>
</body>
</html>
```